Etikett für für Teigtaschen mit Käsefüllung
Zielgruppe
Ich bin Kleinunternehmerin und stelle Teigtaschen her.
Meine Zielgruppe sind Feinkostläden bzw. Endverbraucher
Aufgabenstellung
Ich übersende Ihnen erstmals eine Vorlage der Etikette für Teigtaschen mit Käsefülle.... je nach Fülle, sollte ein tolles Bild für die jeweilige Fülle - in diesem Fall 'Käse' erscheinen. Es sind ja mehrere Käsesorten in der Teigtasche enthalten. Meine LOGO-Daten sind bei Ihnen gespeichert.
Bei der Nährwerttabelle ändern sich noch die Angaben an Gramm....
Die restlichen fünf Banderolen werde ich Ihnen schnellstens nachmailen.
Ich habe keine besonderen Wünsche, deshalb vertraue ich Ihren Designern und bin schon auf die ersten Vorschläge gespannt.

```html
<!DOCTYPE html>
<html lang="de">
<head>
<meta charset="utf-8">
<title>Teigtaschen mit Käsefülle – Etikett</title>
<link href="https://fonts.googleapis.com/css2?family=Fredoka:wght@400;600&family=Poppins:wght@400;600;700&family=Roboto+Condensed:wght@300;400;700&display=swap" rel="stylesheet">
<style>
  :root{
    --leaf:#8cc63f;
    --forest:#2e6b2e;
    --ink:#1a1a1a;
    --rule:#555;
    --paper:#ffffff;
    --trim:#b5b5b5;
    --cheese-light:#f6e27a;
    --cheese-dark:#d9b43a;
  }
  *{box-sizing:border-box;margin:0;padding:0}
  html,body{width:1200px;height:388px;overflow:hidden;background:var(--paper)}
  body{position:relative;font-family:"Roboto Condensed",sans-serif;color:var(--ink)}
  .trim{position:absolute;top:0;bottom:0;width:0;border-left:1px dashed var(--trim)}
  .trim--left{left:27px}.trim--right{left:1173px}
  .label{position:absolute;left:27px;top:32px;width:1146px;height:326px;background:var(--paper)}
  .band-top{position:absolute;left:0;top:0;width:100%;height:3px;background:var(--leaf)}
  .band-mid{position:absolute;left:0;top:173px;width:100%;height:4px;background:var(--leaf)}
  .band-base{position:absolute;left:0;top:180px;width:100%;height:146px;background:var(--forest)}

  .info{position:absolute;left:111px;width:187px;font-size:8.5px;font-weight:300}
  .info strong{font-weight:700}
  .line{display:block;white-space:nowrap;text-align:justify;text-align-last:justify}
  .line--end{text-align-last:left}
  .info--ingredients{top:65px;line-height:15px;border-top:1px solid var(--rule);border-bottom:1px solid var(--rule);padding:5px 0 3px}
  .info--storage{top:139px;line-height:13.5px}
  .info--prep{top:194px;line-height:15px;color:#fff;border-bottom:1px solid rgba(255,255,255,.75);padding-bottom:4px}

  .brand{position:absolute;left:0;right:0;top:26px;display:flex;justify-content:center;align-items:center;gap:5px;font-family:"Poppins",sans-serif;font-size:12px;font-weight:600;color:var(--forest)}
  .brand-dot{width:13px;height:13px;border-radius:50%;background:var(--leaf)}
  .title{position:absolute;left:0;right:0;top:62px;text-align:center;font-family:"Fredoka",sans-serif;font-weight:600;font-size:32px;line-height:40px;color:var(--ink)}
  .subtitle{position:absolute;left:0;right:0;top:96px;line-height:20px;display:flex;justify-content:center;align-items:center;gap:8px;font-family:"Fredoka",sans-serif;font-weight:400;font-size:15px;color:var(--forest)}
  .subtitle::before,.subtitle::after{content:"";width:20px;height:1.5px;background:var(--forest)}
  .product-visual{position:absolute;left:503px;top:135px;width:143px;height:86px;border-radius:6px;background:linear-gradient(135deg,var(--cheese-light),var(--cheese-dark))}

  .claim{position:absolute;left:0;right:0;top:228px;text-align:center;font-family:"Poppins",sans-serif;font-size:8.8px;font-weight:600;line-height:11.5px;color:var(--leaf)}
  .count{position:absolute;left:531px;width:96px;top:270px;text-align:center;font-size:7.5px;line-height:10px;color:#fff;border-top:1px solid rgba(255,255,255,.75);border-bottom:1px solid rgba(255,255,255,.75);padding:4px 0}
  .weight{position:absolute;left:0;right:0;top:292px;text-align:center;font-family:"Poppins",sans-serif;font-size:15px;line-height:20px;font-weight:400;color:var(--leaf)}

  .nutrition{position:absolute;left:851px;top:62px;width:185px;font-family:"Poppins",sans-serif;font-size:6.8px}
  .nutrition h2{font-size:9.5px;line-height:13px;font-weight:600;padding-bottom:2px;border-bottom:3px solid var(--ink)}
  .nutrition table{width:100%;border-collapse:collapse}
  .nutrition td{padding:1px 0;line-height:8.9px;border-bottom:1px solid var(--ink);font-weight:700}
  .nutrition td:last-child{text-align:right}
  .nutrition .sub td{font-weight:400;padding-left:8px}

  .maker{position:absolute;left:853px;width:200px;top:232px;text-align:center;color:#fff;font-style:normal;font-size:7.6px;line-height:11.5px;font-weight:300}
  .maker h3{font-size:9px;line-height:12px;font-weight:700}
  .maker .web{font-weight:700}
</style>
</head>
<body>
  <div class="trim trim--left"></div>
  <div class="trim trim--right"></div>
  <main class="label">
    <div class="band-top"></div>
    <div class="band-mid"></div>
    <div class="band-base"></div>

    <div class="brand"><span class="brand-dot"></span>feinbissen</div>
    <h1 class="title">Teigtaschen</h1>
    <p class="subtitle">mit Käsefülle</p>
    <div class="product-visual" role="img" aria-label="Foto: zwei Käsestücke, Hartkäse und Lochkäse"></div>

    <p class="info info--ingredients">
      <span class="line"><strong>ZUTATEN:</strong> Teig (50%): Dinkelmehl, Hartweizengriess,</span>
      <span class="line">Eier, Olivenöl / Fülle (50%): Käsemischung (Gruyère,</span>
      <span class="line">Emmentaler, Ricotta, Parmesan, Frischkäse), Basilikum,</span>
      <span class="line line--end">Pfeffer, Meersalz</span>
    </p>
    <p class="info info--storage">
      <span class="line line--end"><strong>AUFBEWAHRUNG:</strong> Im Tiefkühlfach*** bei -18°Celsius</span>
      <span class="line line--end">Mindestens haltbar bis - Siehe Rückseite der Etikette</span>
    </p>
    <p class="info info--prep">
      <span class="line"><strong>ZUBEREITUNG:</strong> Grossen Topf mit Salzwasser zum</span>
      <span class="line">Sieden bringen. Die gefrorenen Teigtaschen vorsichtig</span>
      <span class="line">einlegen, Hitze reduzieren, behutsam mit dem</span>
      <span class="line">Holzlöffel einige Male umrühren und max. <strong>8 Minuten</strong></span>
      <span class="line">auf kleinerer Stufe leicht kochen lassen. Teigtaschen</span>
      <span class="line">vorsichtig mit dem Holzlöffel aus dem Wasser</span>
      <span class="line line--end">nehmen und mit entsprechendem Guss anrichten.</span>
    </p>

    <p class="claim">Ohne Konservierungsstoffe,<br>Geschmacksverstärker oder<br>künstliche Aromen</p>
    <p class="count">21 Stück (3-4 Portionen)</p>
    <p class="weight">630g</p>

    <section class="nutrition">
      <h2>Durchschnittliche Nährwerte / 100g</h2>
      <table>
        <tr><td>Brennwerte/Energie</td><td>000 KJ/000 kcal</td></tr>
        <tr><td>Fett</td><td>000 g</td></tr>
        <tr class="sub"><td>davon gesättigte Fettsäuren</td><td>000 g</td></tr>
        <tr><td>Kohlenhydrate</td><td>000 g</td></tr>
        <tr><td>Zucker</td><td>000 g</td></tr>
        <tr><td>Eiweiss</td><td>000 g</td></tr>
        <tr><td>Salz</td><td>000 g</td></tr>
      </table>
    </section>

    <address class="maker">
      <h3>HERSTELLER</h3>
      Helga Kelmaus, Am Anger 7, 6850 Dornbach, Österreich<br>
      T: +43 (0)660 12345678, helkelmaus@postfach.at<br>
      <span class="web">www.feinbissen.at</span>
    </address>
  </main>
</body>
</html>
```